Driftwood Bay Private Yacht Charter "Rack Flyer"

This will be a 4" x 9" Rack flyer that is 4 colors and two sided. This is a Private Yacht charter company that is based in St Thomas, U.S. Virgin Islands. Our main product that I would like to promote on one entire side of the flyer is our Private Luxury Full Day "Gilded Galley". our charter company is unique in the fact we offer customizable itineraries and we offer unique activities that keep the family and groups engaged in fun for the entire day. We would like something with our colors.

Target Market(s)

We are trying to reach an upscale clients that are looking for a Luxury Day Charter experience. these people will be most likely staying in Private Villas or staying at the Halloway Crest or PK Bellmont.

Requirements
Must have
• Contact Information:
Ph: (340) 555-0187
email: Info@driftwoodbayvoyages.example
www.driftwoodbayvoyages.example
One side should Promote our Gilded Galley (Gilded Galley is a trademarked name).
All Guests will receive "Harbor Fizz"
> Up to 12 guests
> Full Brunch Spread to include, Assorted fruit tower, Artesian Waffle Board, Frittata's, Loaded Avocado Toast or an All American Breakfast.
> Specialty Cocktails with Bottle Service options available
List all of our Unique activities to include:
Snorkeling
Underwater WaveGlider
Cliff Diving
Paddleboarding
Towable Activities
TEXT TO BE WRITTEN:
Experience yacht charter service at its Finest!
Sail away with us on a Luxury Charter experience complete with a full brunch spread. During our sail we will take you to the hottest destination spots in the Caribbean surrounding St Thomas and St John. Warm, fresh baked afternoon cookies will be served on the way back from our days journeys. Unlimited water, sodas, beer and rum punch will be provided for the entire group to enjoy throughout the day.
_________________

On side two of the brochure you can refer to the downloaded text. We do not want pricing listed on the flyer

```html
<!DOCTYPE html>
<html lang="en">
<head>
<meta charset="utf-8">
<title>Driftwood Bay Private Yacht Charter – Rack Flyer</title>
<link href="https://fonts.googleapis.com/css2?family=Oswald:wght@400;500;600&family=Roboto+Condensed:wght@400;500&display=swap" rel="stylesheet">
<style>
:root{
  --blue:#1565c8;
  --blue-deep:#0d47a1;
  --navy:#173a8a;
  --red:#e3141b;
  --white:#ffffff;
  --ink:#2a2a2a;
  --stage:#eef0f2;
  --sea:#4aa9d8;
  --sand:#e8d2a8;
}
*{box-sizing:border-box;margin:0;padding:0}
html,body{width:1200px;height:794px;overflow:hidden;background:var(--stage)}
.stage{position:relative;width:1200px;height:794px}
.flyer{position:absolute;top:28px;width:340px;height:738px;background:var(--white);overflow:hidden;font-family:"Roboto Condensed",sans-serif;color:var(--ink)}
.flyer--front{left:217px}
.flyer--back{left:643px}
.abs{position:absolute}
.shapes{position:absolute;left:0;top:0;width:340px;height:738px}
.photo{position:absolute}
.photo--round{border-radius:50%;border:4px solid var(--white);box-shadow:0 2px 8px rgba(0,0,0,.25)}
.brand{top:26px;left:0;width:340px;display:flex;justify-content:center;align-items:center;gap:8px;font-family:"Oswald",sans-serif;font-weight:500;font-size:26px;color:var(--red);letter-spacing:.5px}
.brand__dot{width:12px;height:12px;border-radius:50%;background:var(--blue)}
.badge{left:17px;top:262px;width:146px;height:170px;text-align:center;color:var(--white);font-family:"Oswald",sans-serif;padding-top:14px}
.badge__small{font-size:11px;line-height:14px;text-transform:uppercase}
.badge__mid{font-size:13.5px;line-height:16px;font-weight:500;text-transform:uppercase}
.badge__rule{margin:6px auto 4px;width:100px;height:1px;background:var(--white)}
.badge__title{font-size:29px;line-height:31px;font-weight:500;text-transform:uppercase}
.list{list-style:none}
.list li{display:flex;align-items:center;gap:8px;height:21px}
.list--light li{color:var(--white);font-size:12.5px;font-family:"Oswald",sans-serif;font-weight:400}
.list--dark li{font-size:12px;color:var(--ink)}
.bullet{width:9px;height:9px;flex:none}
.copy{left:20px;width:165px;font-size:10.5px;line-height:14.6px}
.copy p+p{margin-top:14px}
.headline{left:0;top:26px;width:340px;text-align:center;color:var(--white);font-family:"Oswald",sans-serif;font-weight:500;font-size:22px;line-height:29px;text-transform:uppercase}
.pill{left:0;height:20px;padding:0 14px 0 20px;background:var(--red);color:var(--white);font-family:"Oswald",sans-serif;font-size:11.5px;line-height:20px;border-radius:0 10px 10px 0}
.contact{left:0;width:340px;text-align:center}
.contact__title{top:666px;font-family:"Oswald",sans-serif;font-weight:500;font-size:14px;color:var(--navy);text-transform:uppercase}
.contact__row{display:flex;justify-content:center;align-items:center;gap:6px;font-size:10.5px;color:var(--ink)}
.contact__row--first{top:694px}
.contact__row--second{top:714px}
.contact__gap{width:8px}
.contact__at{color:var(--red);font-weight:500;font-size:12px}
.icon{width:11px;height:11px}
</style>
</head>
<body>
<main class="stage">

  <!-- FRONT SIDE -->
  <section class="flyer flyer--front">
    <div class="abs brand"><span>Driftwood Bay</span><span class="brand__dot"></span></div>

    <div class="photo" style="left:0;top:75px;width:340px;height:220px;background:linear-gradient(160deg,#f3d9b0 0%,#9fc3d8 45%,#3c6f8f 100%)" role="img" aria-label="Smiling family giving thumbs up aboard a sailing yacht at sunset"></div>

    <svg class="shapes" viewBox="0 0 340 738" aria-hidden="true">
      <path d="M150,300 C230,270 290,278 340,262 L340,405 C270,425 200,442 120,436 C60,432 25,424 0,432 L0,360 Z" fill="var(--blue)"/>
      <path d="M0,440 C80,420 150,450 230,432 C280,420 315,408 340,402" fill="none" stroke="var(--red)" stroke-width="5"/>
      <path d="M0,448 C80,428 150,458 230,440 C280,428 315,416 340,410 L340,460 L0,460 Z" fill="var(--white)"/>
      <path d="M15,258 H165 V387 L90,436 L15,387 Z" fill="var(--white)"/>
      <path d="M19,262 H161 V384 L90,430 L19,384 Z" fill="var(--red)"/>
      <path d="M0,662 C100,640 240,664 340,642" fill="none" stroke="var(--blue-deep)" stroke-width="4"/>
    </svg>

    <div class="abs badge">
      <div class="badge__small">Experience</div>
      <div class="badge__mid">Yacht Charter Service</div>
      <div class="badge__small">At its finest!</div>
      <div class="badge__rule"></div>
      <div class="badge__title">Gilded<br>Galley</div>
    </div>

    <ul class="abs list list--light" style="left:180px;top:297px">
      <li><svg class="bullet" viewBox="0 0 10 10"><path d="M2,1 L8,5 L2,9 Z" fill="#fff"/></svg>Snorkeling</li>
      <li><svg class="bullet" viewBox="0 0 10 10"><path d="M2,1 L8,5 L2,9 Z" fill="#fff"/></svg>Underwater WaveGlider</li>
      <li><svg class="bullet" viewBox="0 0 10 10"><path d="M2,1 L8,5 L2,9 Z" fill="#fff"/></svg>Cliff Diving</li>
      <li><svg class="bullet" viewBox="0 0 10 10"><path d="M2,1 L8,5 L2,9 Z" fill="#fff"/></svg>Paddleboarding</li>
      <li><svg class="bullet" viewBox="0 0 10 10"><path d="M2,1 L8,5 L2,9 Z" fill="#fff"/></svg>Towable Activities</li>
    </ul>

    <div class="photo photo--round" style="left:196px;top:418px;width:108px;height:108px;background:radial-gradient(circle,#6fd0e8,#1a7fb0)" role="img" aria-label="Snorkeler in mask underwater"></div>
    <div class="photo photo--round" style="left:195px;top:528px;width:120px;height:120px;background:linear-gradient(180deg,#cfe6f2 0%,#f1f1f1 40%,#3ab7d0 70%,#e8d2a8 100%)" role="img" aria-label="White catamaran anchored in turquoise water"></div>

    <div class="abs copy" style="top:448px">
      <p>Sail away with us on a Luxury Charter experience complete with a full brunch spread. During our sail we will take you to the hottest destination spots in the Caribbean surrounding St Thomas and St John.</p>
      <p>Warm, fresh baked afternoon cookies will be served on the way back from our days journeys. Unlimited water, sodas, beer and rum punch will be provided for the entire group to enjoy throughout the day.</p>
    </div>

    <div class="abs contact contact__title">Contact Us</div>
    <div class="abs contact contact__row contact__row--first">
      <svg class="icon" viewBox="0 0 12 12"><path d="M3,1 L5,3.5 L4,5 C5,7 6,8 7.5,8.5 L9,7.5 L11,9.5 L9.5,11 C5,10.5 1.5,7 1,2.5 Z" fill="var(--red)"/></svg>
      <span>(340) 555-0187</span><span class="contact__gap"></span>
      <span class="contact__at">@</span><span>Info@driftwoodbayvoyages.example</span>
    </div>
    <div class="abs contact contact__row contact__row--second">
      <svg class="icon" viewBox="0 0 12 12"><circle cx="6" cy="6" r="5" fill="none" stroke="var(--red)" stroke-width="1.2"/><ellipse cx="6" cy="6" rx="2.2" ry="5" fill="none" stroke="var(--red)" stroke-width="1"/><path d="M1,6 H11" stroke="var(--red)" stroke-width="1"/></svg>
      <span>www.driftwoodbayvoyages.example</span>
    </div>
  </section>

  <!-- BACK SIDE -->
  <section class="flyer flyer--back">
    <div class="photo" style="left:0;top:470px;width:340px;height:185px;background:linear-gradient(180deg,rgba(255,255,255,1) 0%,rgba(205,228,242,.9) 25%,#7cc0de 60%,#3b92b8 100%)" role="img" aria-label="Two girls with raised arms overlooking a bay with anchored boats"></div>

    <svg class="shapes" viewBox="0 0 340 738" aria-hidden="true">
      <path d="M0,0 H340 V245 C300,238 265,212 210,195 C150,178 80,165 0,190 Z" fill="var(--blue)"/>
      <path d="M0,180 C80,152 150,165 215,198 C265,224 305,248 340,242" fill="none" stroke="var(--white)" stroke-width="10"/>
      <path d="M0,184 C80,156 150,170 215,204 C265,230 305,254 340,248" fill="none" stroke="var(--red)" stroke-width="5"/>
      <path d="M0,662 C100,640 240,664 340,642" fill="none" stroke="var(--blue-deep)" stroke-width="4"/>
      <path d="M0,666 C100,644 240,668 340,646 L340,738 L0,738 Z" fill="var(--white)"/>
    </svg>

    <div class="abs headline">Harbor Fizz<br>Private Luxury Full Day Charter<br>8:30 AM - 12:00 to 1:00 - 4:30 PM</div>

    <div class="photo photo--round" style="left:186px;top:133px;width:134px;height:134px;background:linear-gradient(160deg,#e9eef2,#c79a6a 60%,#8a5a34)" role="img" aria-label="Couple toasting with drinks at a brunch table on deck"></div>
    <div class="photo photo--round" style="left:185px;top:265px;width:136px;height:136px;background:radial-gradient(circle,#bfe9f2,#3aa5d6 70%,#1b6fa8)" role="img" aria-label="Blue swim fins in clear shallow water"></div>

    <ul class="abs list list--dark" style="left:22px;top:199px">
      <li><svg class="bullet" viewBox="0 0 10 10"><path d="M2,1 L8,5 L2,9 Z" fill="var(--red)"/></svg>Up to 12 guests</li>
      <li><svg class="bullet" viewBox="0 0 10 10"><path d="M2,1 L8,5 L2,9 Z" fill="var(--red)"/></svg>Specialty Cocktails with Bottle</li>
      <li><svg class="bullet" viewBox="0 0 10 10"><path d="M2,1 L8,5 L2,9 Z" fill="var(--red)"/></svg>Service options available</li>
    </ul>

    <div class="abs pill" style="top:288px">Full Brunch Spread:</div>
    <ul class="abs list list--dark" style="left:22px;top:312px">
      <li><svg class="bullet" viewBox="0 0 10 10"><path d="M2,1 L8,5 L2,9 Z" fill="var(--red)"/></svg>Assorted fruit tower</li>
      <li><svg class="bullet" viewBox="0 0 10 10"><path d="M2,1 L8,5 L2,9 Z" fill="var(--red)"/></svg>Artesian Waffle Board</li>
      <li><svg class="bullet" viewBox="0 0 10 10"><path d="M2,1 L8,5 L2,9 Z" fill="var(--red)"/></svg>Frittata's, Loaded Avocado</li>
      <li><svg class="bullet" viewBox="0 0 10 10"><path d="M2,1 L8,5 L2,9 Z" fill="var(--red)"/></svg>Toast or an All American Breakfast</li>
    </ul>

    <div class="abs pill" style="top:413px">List all of our Unique activities to include:</div>
    <ul class="abs list list--dark" style="left:22px;top:437px">
      <li><svg class="bullet" viewBox="0 0 10 10"><path d="M2,1 L8,5 L2,9 Z" fill="var(--red)"/></svg>Snorkeling</li>
      <li><svg class="bullet" viewBox="0 0 10 10"><path d="M2,1 L8,5 L2,9 Z" fill="var(--red)"/></svg>Underwater WaveGlider</li>
      <li><svg class="bullet" viewBox="0 0 10 10"><path d="M2,1 L8,5 L2,9 Z" fill="var(--red)"/></svg>Cliff Diving</li>
      <li><svg class="bullet" viewBox="0 0 10 10"><path d="M2,1 L8,5 L2,9 Z" fill="var(--red)"/></svg>Paddleboarding</li>
      <li><svg class="bullet" viewBox="0 0 10 10"><path d="M2,1 L8,5 L2,9 Z" fill="var(--red)"/></svg>Towable Activities</li>
    </ul>

    <div class="abs contact contact__title">Contact Us</div>
    <div class="abs contact contact__row contact__row--first">
      <svg class="icon" viewBox="0 0 12 12"><path d="M3,1 L5,3.5 L4,5 C5,7 6,8 7.5,8.5 L9,7.5 L11,9.5 L9.5,11 C5,10.5 1.5,7 1,2.5 Z" fill="var(--red)"/></svg>
      <span>(340) 555-0187</span><span class="contact__gap"></span>
      <span class="contact__at">@</span><span>Info@driftwoodbayvoyages.example</span>
    </div>
    <div class="abs contact contact__row contact__row--second">
      <svg class="icon" viewBox="0 0 12 12"><circle cx="6" cy="6" r="5" fill="none" stroke="var(--red)" stroke-width="1.2"/><ellipse cx="6" cy="6" rx="2.2" ry="5" fill="none" stroke="var(--red)" stroke-width="1"/><path d="M1,6 H11" stroke="var(--red)" stroke-width="1"/></svg>
      <span>www.driftwoodbayvoyages.example</span>
    </div>
  </section>

</main>
</body>
</html>
```